Orthodontist Needs Promotional Discount Postcard

5.5 x 8.5 Horizontal 2-Sided Postcard for mailing.
Images & Logo on both sides okay; must be free stock Images from legit sources only, or use attached images. See our website for information, ShoreLaneSmiles.com
Context to include:
New Patient Special $500 off Braces or Clear Aligners
Cannot be combined with any other discounts.
Major dental insurance plans and Cara-Plan accepted
Affordable payment options are available
Call to schedule your free consultation
Present this new patient offer to receive your discount.
Offer ends January 31, 2022.
805-472-9186 www. ShoreLaneSmiles.com
462 N. Harlow Street, Suite B, Ventura, CA 93001-2718
office@shorelanesmiles.com

```html
<!DOCTYPE html>
<html lang="en">
<head>
<meta charset="utf-8">
<title>Shore Lane Smiles – New Patient Postcard</title>
<link href="https://fonts.googleapis.com/css2?family=Poppins:ital,wght@0,300;0,400;0,500;0,600;0,700;1,600&family=Yellowtail&display=swap" rel="stylesheet">
<style>
  :root{
    --page:#dcf0fa;
    --blue:#1c9ad8;
    --deep:#0a7ccb;
    --sky:#d6edf9;
    --teal:#7ccfd0;
    --ink:#1c1c1c;
    --white:#ffffff;
  }
  *{box-sizing:border-box;margin:0;padding:0}
  html,body{width:941px;height:1200px;overflow:hidden}
  body{background:var(--page);font-family:"Poppins",sans-serif;color:var(--ink);position:relative}
  .card{position:absolute;left:83px;width:776px;height:510px;overflow:hidden;background:var(--white);box-shadow:0 8px 18px rgba(20,80,120,.18)}
  .card--front{top:70px}
  .card--back{top:620px}
  .abs{position:absolute}
  .card-bg{position:absolute;inset:0}

  /* brand name */
  .brand{position:absolute;display:flex;align-items:center;gap:10px}
  .brand__dot{width:46px;height:46px;border-radius:50%;background:var(--blue)}
  .brand__name{font-weight:600;font-size:19px;color:var(--blue);line-height:1;white-space:nowrap}

  /* front */
  .tagline{left:55px;top:156px;font-weight:600;font-style:italic;font-size:20px;white-space:nowrap}
  .script{left:50px;top:180px;font-family:"Yellowtail",cursive;font-size:60px;color:var(--blue);line-height:1;white-space:nowrap}
  .offer{left:42px;top:261px;width:415px;height:160px;background:var(--white);box-shadow:0 3px 10px rgba(0,0,0,.12);border-radius:6px 6px 0 0}
  .special{position:absolute;left:16px;top:15px;width:179px;height:90px;border-radius:5px;overflow:hidden;background:var(--blue);text-align:center;color:var(--white)}
  .special__label{background:var(--teal);height:26px;line-height:27px;font-weight:500;font-size:12px;letter-spacing:.3px;white-space:nowrap}
  .special__amount{font-weight:700;font-size:36px;line-height:40px;margin-top:2px;white-space:nowrap}
  .special__product{font-size:12.5px;line-height:16px;white-space:nowrap}
  .perk{position:absolute;left:210px;display:flex;align-items:center;gap:12px;font-size:10.5px;line-height:13px;white-space:nowrap}
  .perk svg{flex:none}
  .offer__rule{position:absolute;left:202px;right:12px;top:104px;height:1px;background:#ccc}
  .offer__terms{position:absolute;top:113px;left:18px;right:8px;display:flex;font-size:9.6px;line-height:14px;white-space:nowrap}
  .offer__terms span:last-child{margin-left:7px;padding-left:7px;border-left:1px solid #bbb}
  .offer__present{position:absolute;left:0;right:0;bottom:0;height:28px;line-height:28px;background:linear-gradient(90deg,var(--teal),var(--blue));color:var(--white);font-size:9.4px;letter-spacing:1.2px;padding-left:18px;white-space:nowrap;overflow:hidden}
  .photo{position:absolute}
  .contact{color:var(--white);font-size:11.5px;line-height:20px;display:flex;gap:7px;white-space:nowrap}
  .contact svg{flex:none;margin-top:5px}
  .call{color:var(--white);font-size:12.5px;white-space:nowrap}
  .call b{font-weight:700}
  .phone{display:flex;align-items:center;gap:12px;color:var(--white);font-weight:700;font-size:30px;letter-spacing:.5px;white-space:nowrap}
  .phone__icon{width:34px;height:34px;border-radius:50%;background:linear-gradient(135deg,#fff,#bfe3f5);display:flex;align-items:center;justify-content:center}

  /* back */
  .doctor-photo{left:32px;top:34px;width:111px;height:111px;border-radius:50%;border:3px solid var(--white);background:linear-gradient(180deg,#b9c9d4,#d8c39a 60%,#2f3c58)}
  .eyebrow{left:157px;top:43px;font-size:9.5px;letter-spacing:1.4px;color:#e6f4fc;white-space:nowrap}
  .eyebrow-rule{left:157px;top:62px;width:45px;height:2px;background:var(--teal)}
  .doctor-name{left:157px;top:70px;font-weight:700;font-size:20px;line-height:23px;color:var(--white);white-space:nowrap}
  .doctor-title{left:157px;top:120px;font-size:10.5px;color:var(--white);white-space:nowrap}
  .tech-heading{left:29px;top:164px;font-weight:700;font-size:16px;line-height:19px;color:var(--white);white-space:nowrap;z-index:2}
  .tech-copy{left:29px;top:208px;font-size:8.9px;line-height:13.6px;color:var(--white);white-space:nowrap;z-index:2}
  .robot-photo{left:322px;top:160px;width:90px;height:228px;border-radius:30px 30px 10px 10px;background:linear-gradient(160deg,#f4f5f6,#cfd3d6)}
  .feature{position:absolute;display:flex;align-items:center;gap:9px;color:var(--white);font-size:10.5px;line-height:11.5px;white-space:nowrap;z-index:2}
  .feature__icon{width:28px;height:28px;border-radius:50%;background:var(--white);display:flex;align-items:center;justify-content:center}
  .back-links{left:35px;top:467px;display:flex;gap:10px;color:var(--white);font-size:10.5px;white-space:nowrap}
  .back-links span{display:flex;align-items:center;gap:5px}
  .back-links .sep{width:1px;height:20px;background:rgba(255,255,255,.5);margin-top:-3px}
  .stamp{left:673px;top:37px;width:68px;height:68px;border:1px solid #333}
  .address-line{left:431px;width:305px;height:1px;background:#333}
</style>
</head>
<body>

<!-- FRONT -->
<section class="card card--front">
  <svg class="card-bg" width="776" height="510" viewBox="0 0 776 510">
    <defs>
      <linearGradient id="skyFade" x1="0" y1="0" x2="1" y2="1">
        <stop offset="0" stop-color="#bfe2f6"/><stop offset="1" stop-color="#eef8fd"/>
      </linearGradient>
      <linearGradient id="bandFade" x1="0" y1="0" x2="1" y2="1">
        <stop offset="0" stop-color="#1ea3df"/><stop offset="1" stop-color="#0a7ccb"/>
      </linearGradient>
      <linearGradient id="warmPhoto" x1="0" y1="0" x2="1" y2="1">
        <stop offset="0" stop-color="#f1e3d2"/><stop offset=".5" stop-color="#d59a68"/><stop offset="1" stop-color="#c0682c"/>
      </linearGradient>
    </defs>
    <rect width="776" height="510" fill="url(#skyFade)"/>
    <path d="M345 0H776V318H360C380 240 330 190 315 120C305 60 325 25 345 0Z" fill="url(#warmPhoto)" role="img" aria-label="Photo of a smiling woman framing her face with her hands"/>
    <path d="M0 0H350C320 70 300 120 200 124C120 127 40 148 0 190Z" fill="#ffffff"/>
    <path d="M0 190C40 150 120 130 200 128C300 124 320 70 352 0" fill="none" stroke="#1592d4" stroke-width="7"/>
    <rect y="318" width="776" height="192" fill="url(#bandFade)"/>
  </svg>

  <div class="brand" style="left:36px;top:50px">
    <span class="brand__dot"></span><span class="brand__name">Shore Lane Smiles</span>
  </div>

  <p class="abs tagline">Start your day with</p>
  <p class="abs script">New Smile</p>

  <div class="abs offer">
    <div class="special">
      <div class="special__label">NEW PATIENT SPECIAL</div>
      <div class="special__amount">$500 off</div>
      <div class="special__product">Braces or Clear Aligners</div>
    </div>
    <div class="perk" style="top:22px">
      <svg width="25" height="28" viewBox="0 0 25 28"><path d="M12.5 1L23 5v8c0 7-5 12-10.5 14C7 25 2 20 2 13V5z" fill="none" stroke="#1c9ad8" stroke-width="1.4"/><circle cx="12.5" cy="14" r="5" fill="none" stroke="#1c9ad8" stroke-width="1.2"/><path d="M10 14l2 2 3.5-4" fill="none" stroke="#1c9ad8" stroke-width="1.2"/></svg>
      <span>Major dental insurance plans<br>&amp; Cara-Plan accepted</span>
    </div>
    <div class="perk" style="top:63px">
      <svg width="25" height="22" viewBox="0 0 25 22"><rect x="1" y="1" width="19" height="13" rx="2" fill="none" stroke="#1c9ad8" stroke-width="1.3"/><rect x="5" y="7" width="19" height="13" rx="2" fill="#fff" stroke="#1c9ad8" stroke-width="1.3"/><path d="M8 16h5M19 16h2" stroke="#1c9ad8" stroke-width="1.3"/></svg>
      <span>Affordable payment options<br>are available</span>
    </div>
    <div class="offer__rule"></div>
    <div class="offer__terms"><span>Cannot be combined with any other discounts.</span><span>Offer ends <b>January 31, 2022.</b></span></div>
    <div class="offer__present">PRESENT THIS NEW PATIENT OFFER TO RECEIVE YOUR DISCOUNT</div>
  </div>

  <div class="photo" style="left:469px;top:261px;width:268px;height:139px;background:#fff;padding:2px;display:flex;gap:3px">
    <div style="flex:1;background:linear-gradient(160deg,#f4e6e2,#e3b3ad)" role="img" aria-label="Close-up photo of a person fitting a clear aligner"></div>
    <div style="flex:1;background:linear-gradient(160deg,#f6d9d6,#d98c89)" role="img" aria-label="Close-up photo of a smile with metal braces"></div>
  </div>

  <div class="abs contact" style="left:45px;top:444px">
    <svg width="9" height="11" viewBox="0 0 9 11"><path d="M4.5 0A4.2 4.2 0 0 0 .3 4.2C.3 7.3 4.5 11 4.5 11s4.2-3.7 4.2-6.8A4.2 4.2 0 0 0 4.5 0z" fill="#fff"/><circle cx="4.5" cy="4.2" r="1.5" fill="#1c9ad8"/></svg>
    <span>462 N. Harlow Street, Suite B,<br>Ventura, CA 93001-2718</span>
  </div>
  <div class="abs contact" style="left:263px;top:444px;flex-direction:column;gap:2px">
    <span style="display:flex;gap:9px"><svg width="10" height="8" viewBox="0 0 10 8" style="margin-top:6px"><rect width="10" height="8" rx="1" fill="#fff"/><path d="M0 1l5 3.5L10 1" fill="none" stroke="#1c9ad8"/></svg>office@shorelanesmiles.com</span>
    <span style="display:flex;gap:9px"><svg width="10" height="10" viewBox="0 0 10 10" style="margin-top:5px"><circle cx="5" cy="5" r="4.4" fill="none" stroke="#fff"/><path d="M.6 5h8.8M5 .6c-2.5 2.6-2.5 6.2 0 8.8M5 .6c2.5 2.6 2.5 6.2 0 8.8" fill="none" stroke="#fff" stroke-width=".8"/></svg>ShoreLaneSmiles.com</span>
  </div>

  <p class="abs call" style="left:472px;top:416px">Call to schedule your <b>FREE CONSULTATION</b></p>
  <div class="abs phone" style="left:472px;top:440px">
    <span class="phone__icon"><svg width="16" height="16" viewBox="0 0 24 24"><path d="M6.6 10.8a15 15 0 0 0 6.6 6.6l2.2-2.2a1 1 0 0 1 1-.25 11.4 11.4 0 0 0 3.6.57 1 1 0 0 1 1 1V20a1 1 0 0 1-1 1A17 17 0 0 1 3 4a1 1 0 0 1 1-1h3.5a1 1 0 0 1 1 1c0 1.25.2 2.45.57 3.57a1 1 0 0 1-.25 1z" fill="#1c9ad8"/></svg></span>
    <span>805-472-9186</span>
  </div>
</section>

<!-- BACK -->
<section class="card card--back">
  <svg class="card-bg" width="776" height="510" viewBox="0 0 776 510">
    <defs>
      <linearGradient id="backBlue" x1="0" y1="0" x2="0" y2="1">
        <stop offset="0" stop-color="#20a4e0"/><stop offset="1" stop-color="#0a7ccb"/>
      </linearGradient>
    </defs>
    <path d="M0 0H460C400 60 360 150 355 260C352 360 370 440 390 510H0Z" fill="#8fd6d4"/>
    <path d="M0 0H425C370 60 335 150 340 260C345 360 370 440 380 510H0Z" fill="url(#backBlue)"/>
  </svg>

  <div class="abs doctor-photo" role="img" aria-label="Portrait photo of the orthodontist"></div>
  <p class="abs eyebrow">INTERNATIONALLY RECOGNIZED</p>
  <div class="abs eyebrow-rule"></div>
  <h2 class="abs doctor-name">Daniel R Whitford,<br>DDS, MS</h2>
  <p class="abs doctor-title">Certified Orthodontic Specialist</p>

  <div class="abs robot-photo" role="img" aria-label="Photo of a white robotic arm"></div>

  <h3 class="abs tech-heading">Superior Technology Developed<br>Right Here</h3>
  <p class="abs tech-copy">Dr. Whitford engineered and developed robotically<br>assisted orthodontic technology to finally bring his full<br>vision to reality. True 3D diagnosis allows us to get all parts of<br>your teeth in the correct position - Including the roots. This leads<br>to more long term stability of your results.</p>

  <div class="feature" style="left:33px;top:297px"><span class="feature__icon"><svg width="16" height="14" viewBox="0 0 16 14"><rect x="1" y="1" width="14" height="9" rx="1" fill="none" stroke="#1c9ad8"/><path d="M3 8l2-3 2 2 2-4 2 3 2-1M6 13h4M8 10v3" fill="none" stroke="#1c9ad8"/></svg></span><span>3D<br>Diagnosis</span></div>
  <div class="feature" style="left:196px;top:297px"><span class="feature__icon"><svg width="16" height="16" viewBox="0 0 16 16"><circle cx="8" cy="8" r="3" fill="none" stroke="#1c9ad8"/><path d="M8 1v3M8 12v3M1 8h3M12 8h3M3 3l2 2M11 11l2 2M13 3l-2 2M5 11l-2 2" stroke="#1c9ad8"/></svg></span><span>Robotic<br>Assistance</span></div>
  <div class="feature" style="left:33px;top:342px"><span class="feature__icon"><svg width="12" height="16" viewBox="0 0 12 16"><rect x="1" y="1" width="10" height="14" rx="2" fill="none" stroke="#1c9ad8"/><path d="M5 13h2" stroke="#1c9ad8"/></svg></span><span>Virtual<br>Appointments</span></div>
  <div class="feature" style="left:196px;top:342px"><span class="feature__icon"><svg width="18" height="12" viewBox="0 0 18 12"><path d="M1 3c0-2 3-2 4 0 1-2 4-2 4 0 0-2 3-2 4 0 1-2 4-2 4 0v3c0 4-2 5-3 5-1-3-2-3-3 0-1 0-2-1-2-3-1 2-2 3-3 3s-2-1-2-3c-1 2-2 3-3 3-1 0-3-1-3-5z" fill="none" stroke="#1c9ad8" stroke-width=".9"/><path d="M1 5h16" stroke="#1c9ad8" stroke-width=".9"/></svg></span><span>Advanced<br>Brackets</span></div>

  <p class="abs call" style="left:35px;top:400px">Call to schedule your <b>FREE CONSULTATION</b></p>
  <div class="abs phone" style="left:35px;top:423px">
    <span class="phone__icon"><svg width="16" height="16" viewBox="0 0 24 24"><path d="M6.6 10.8a15 15 0 0 0 6.6 6.6l2.2-2.2a1 1 0 0 1 1-.25 11.4 11.4 0 0 0 3.6.57 1 1 0 0 1 1 1V20a1 1 0 0 1-1 1A17 17 0 0 1 3 4a1 1 0 0 1 1-1h3.5a1 1 0 0 1 1 1c0 1.25.2 2.45.57 3.57a1 1 0 0 1-.25 1z" fill="#1c9ad8"/></svg></span>
    <span>805-472-9186</span>
  </div>
  <div class="abs back-links">
    <span><svg width="9" height="7" viewBox="0 0 10 8"><rect width="10" height="8" rx="1" fill="#fff"/><path d="M0 1l5 3.5L10 1" fill="none" stroke="#1c9ad8"/></svg>office@shorelanesmiles.com</span>
    <span class="sep"></span>
    <span><svg width="9" height="9" viewBox="0 0 10 10"><circle cx="5" cy="5" r="4.4" fill="none" stroke="#fff"/><path d="M.6 5h8.8M5 .6c-2.5 2.6-2.5 6.2 0 8.8M5 .6c2.5 2.6 2.5 6.2 0 8.8" fill="none" stroke="#fff" stroke-width=".8"/></svg>ShoreLaneSmiles.com</span>
  </div>

  <div class="brand" style="left:427px;top:55px">
    <span class="brand__dot"></span><span class="brand__name">Shore Lane Smiles</span>
  </div>
  <div class="abs stamp"></div>
  <div class="abs address-line" style="top:310px"></div>
  <div class="abs address-line" style="top:355px"></div>
  <div class="abs address-line" style="top:400px"></div>
  <div class="abs address-line" style="top:445px"></div>
</section>

</body>
</html>
```